Velvet Dare Age Verification Landing Page

To create a visually appealing design for the landing page of the adult game "Velvet Dare" that confirms the visitor's age.
The design should have a simple and visually appealing look that focuses on two buttons labeled "Yes" and "No". The purpose of the page is to confirm that the visitor is 18 years of age or older before accessing the game's content. Responsive design that works well on desktop and mobile devices. The final output should be delivered in PSD, AI, or Sketch format, along with any necessary images or assets.
I have also attached examples.

```html
<!DOCTYPE html>
<html lang="en">
<head>
<meta charset="utf-8">
<title>Velvet Dare – Age Verification</title>
<link rel="stylesheet" href="https://fonts.googleapis.com/css2?family=Comfortaa:wght@500;600;700&display=swap">
<style>
  :root {
    --bg-deep: #050404;
    --bg-warm: #3a2b22;
    --bg-mid: #1c1512;
    --brand-purple: #9b5aa3;
    --frame-magenta: #c417c4;
    --frame-violet: #9a5aa6;
    --card-top: #ffffff;
    --card-bottom: #dadada;
    --ink: #111111;
    --button-text: #ffffff;
  }
  * { margin: 0; padding: 0; box-sizing: border-box; }
  html, body {
    width: 1200px;
    height: 675px;
    overflow: hidden;
    background: var(--bg-deep);
  }
  .age-gate {
    position: relative;
    width: 1200px;
    height: 675px;
    overflow: hidden;
    font-family: "Comfortaa", sans-serif;
  }
  .hero-backdrop {
    position: absolute;
    inset: 0;
    background:
      radial-gradient(ellipse 300px 340px at 590px 290px, var(--bg-warm) 0%, var(--bg-mid) 55%, transparent 100%),
      radial-gradient(ellipse 200px 260px at 300px 320px, #2b2b28 0%, transparent 100%),
      linear-gradient(90deg, #0a0908 0%, #15110f 45%, #080605 75%, #020202 100%);
  }
  .brand-name {
    position: absolute;
    left: 0;
    width: 1230px;
    top: 100px;
    text-align: center;
    font-size: 66px;
    font-weight: 600;
    color: var(--brand-purple);
    letter-spacing: 1px;
  }
  .card-frame {
    position: absolute;
    left: 0;
    top: 0;
  }
  .verify-card {
    position: absolute;
    left: 310px;
    top: 245px;
    width: 580px;
    height: 274px;
    border-radius: 28px;
    background: linear-gradient(180deg, var(--card-top) 0%, var(--card-bottom) 100%);
    text-align: center;
    color: var(--ink);
  }
  .verify-rule {
    position: absolute;
    left: 0;
    width: 100%;
    top: 73px;
    font-size: 19px;
    font-weight: 500;
  }
  .verify-question {
    position: absolute;
    left: 0;
    width: 100%;
    top: 112px;
    font-size: 21px;
    font-weight: 600;
  }
  .choice {
    position: absolute;
    top: 179px;
    height: 47px;
    border-radius: 15px;
    background: var(--brand-purple);
    color: var(--button-text);
    font-family: "Comfortaa", sans-serif;
    font-size: 19px;
    font-weight: 600;
    border: none;
    line-height: 47px;
  }
  .choice-yes { left: 124px; width: 110px; }
  .choice-no { left: 313px; width: 105px; }
</style>
</head>
<body>
<main class="age-gate">
  <div class="hero-backdrop" role="img" aria-label="Soft-focus dark photograph of a blonde woman behind the age check"></div>

  <h1 class="brand-name">Velvet Dare</h1>

  <svg class="card-frame" width="1200" height="675" viewBox="0 0 1200 675" aria-hidden="true">
    <defs>
      <linearGradient id="frameStroke" x1="0" y1="0" x2="1" y2="1">
        <stop offset="0" stop-color="var(--frame-magenta)"/>
        <stop offset="1" stop-color="var(--frame-violet)"/>
      </linearGradient>
    </defs>
    <rect x="284" y="248" width="633" height="266" rx="28" ry="28"
          fill="none" stroke="url(#frameStroke)" stroke-width="1.6"
          transform="rotate(2.65 600 381)"/>
  </svg>

  <section class="verify-card">
    <p class="verify-rule">To enter Velvet Dare you must be 18 or older</p>
    <p class="verify-question">Confirm that you’re 18 year old !</p>
    <button class="choice choice-yes" type="button">Yes</button>
    <button class="choice choice-no" type="button">No</button>
  </section>
</main>
</body>
</html>
```